Commercial Landscaping Flyer Needed

Looking for a flyer design to showcase what we offer for commercial landscape Installations. We want this to illustrate what sets us apart from our competitors. Include our EMR Safety rating of .72, that our average commercial landscape installation size is $215,000 with our largest completed in 2020 being $1,375,590. We have backgrounds in commercial design and installation and help our customers with Value Engineering Strategies. Since incorporating in 2005, we have an average employment retention length of 8 years. We want this flyer to show our commercial clients that we mean business and are dedicated to making their project happen on time, run efficiently, and we do excellent work.

Need extra days to review

```html
<!DOCTYPE html>
<html lang="en">
<head>
<meta charset="utf-8">
<title>Verdant Grade Inc. – Commercial Landscaping Flyer</title>
<link rel="stylesheet" href="https://fonts.googleapis.com/css2?family=Ubuntu:wght@400;500;700&family=Open+Sans:wght@400;700&display=swap">
<style>
  :root {
    --backdrop: #dcdddc;
    --ink: #1d1d1d;
    --lime: #bed22a;
    --lime-dark: #9fb51c;
    --white: #ffffff;
    --heading-font: "Ubuntu", sans-serif;
    --body-font: "Open Sans", sans-serif;
  }
  * { margin: 0; padding: 0; box-sizing: border-box; }
  html, body { width: 957px; height: 1200px; overflow: hidden; }
  body { background: var(--backdrop); position: relative; font-family: var(--body-font); }

  .flyer {
    position: absolute; left: 99px; top: 109px;
    width: 758px; height: 981px;
    background: var(--ink); overflow: hidden;
    border: 1px solid #9a9a9a;
  }

  .hero-photo {
    position: absolute; left: 0; top: 0; width: 758px; height: 560px;
    background:
      radial-gradient(ellipse at 28% 55%, #4d8a2c 0%, rgba(77,138,44,0) 45%),
      radial-gradient(ellipse at 62% 40%, #c9c2b4 0%, rgba(201,194,180,0) 40%),
      radial-gradient(ellipse at 70% 58%, #a9776a 0%, rgba(169,119,106,0) 30%),
      radial-gradient(ellipse at 8% 30%, #d9c232 0%, rgba(217,194,50,0) 30%),
      linear-gradient(135deg, #5a5e55 0%, #3f6a2c 45%, #6d6a5c 70%, #3c4a34 100%);
  }

  .wave { position: absolute; left: 0; top: 0; width: 758px; height: 981px; }

  .logo {
    position: absolute; left: 560px; top: 18px;
    width: 170px; height: 110px; border-radius: 50%;
    background: var(--lime); border: 3px solid var(--ink);
    display: flex; flex-direction: column; align-items: center; justify-content: center;
    color: var(--ink); font-family: var(--heading-font); font-weight: 700;
  }
  .logo-name { font-size: 20px; line-height: 1; letter-spacing: -0.3px; }
  .logo-tagline { font-size: 7px; letter-spacing: 1.3px; margin-top: 6px; }

  .project-photo {
    position: absolute; width: 178px; height: 178px; border-radius: 50%;
    border: 2px solid var(--lime); padding: 3px; background: var(--ink);
  }
  .project-photo span { display: block; width: 100%; height: 100%; border-radius: 50%; }
  .project-photo--roadside { left: 35px; top: 433px; }
  .project-photo--roadside span { background: linear-gradient(180deg, #7fa6d8 0%, #a9c4e0 33%, #4f7a37 45%, #a08f7e 65%, #cfcac3 100%); }
  .project-photo--clubhouse { left: 298px; top: 355px; }
  .project-photo--clubhouse span { background: linear-gradient(180deg, #c4c7c9 0%, #8f949a 40%, #3e6e2c 62%, #d98aa0 72%, #5fa53a 100%); }
  .project-photo--station { left: 527px; top: 347px; }
  .project-photo--station span { background: linear-gradient(160deg, #1d6f44 0%, #cfd5d8 30%, #a38f7d 55%, #8d7c6c 80%, #b59c84 100%); }

  .markets {
    position: absolute; left: 250px; top: 568px; width: 460px;
    font-family: var(--heading-font); font-weight: 700; color: var(--lime);
    font-size: 19px; line-height: 24px; text-align: center; letter-spacing: 0.2px;
  }
  .markets .dot { margin: 0 9px; }

  .section-title {
    position: absolute; left: 37px;
    font-family: var(--heading-font); font-weight: 700; color: var(--lime);
    font-size: 22px; line-height: 1; padding-bottom: 3px;
    border-bottom: 2px solid var(--lime);
  }
  .section-title--about { top: 635px; width: 130px; }
  .section-title--services { top: 751px; width: 174px; }

  .about-text {
    position: absolute; left: 37px; top: 662px; width: 690px;
    color: var(--white); font-size: 12.2px; line-height: 17px;
  }
  .about-text strong { font-weight: 700; }

  .service {
    position: absolute; display: flex; align-items: center;
    color: var(--white); font-family: var(--body-font); font-size: 16.5px; letter-spacing: 0.2px;
  }
  .service svg { width: 36px; height: 36px; margin-right: 14px; }
  .service--turf { left: 36px; top: 787px; }
  .service--hardscape { left: 36px; top: 829px; }
  .service--irrigation { left: 280px; top: 787px; }
  .service--landscape { left: 280px; top: 829px; }
  .service--irrigation svg, .service--landscape svg { margin-right: 22px; }

  .safety-badge { position: absolute; left: 592px; top: 745px; width: 132px; height: 115px; }

  .call-bar {
    position: absolute; left: 115px; top: 880px; width: 530px; height: 28px;
    background: var(--lime); border-radius: 14px;
    display: flex; align-items: center; justify-content: center;
    font-family: var(--body-font); font-size: 13.5px; color: var(--ink); white-space: nowrap;
  }
  .call-bar strong { font-weight: 700; }

  .contact-line {
    position: absolute; left: 115px; top: 922px; width: 540px;
    display: flex; align-items: center; gap: 16px;
    color: var(--white); font-size: 11px; white-space: nowrap;
  }
  .contact-item { display: flex; align-items: center; gap: 7px; }
  .contact-item svg { width: 14px; height: 14px; }

  .grass-strip {
    position: absolute; left: 0; bottom: 0; width: 758px; height: 44px;
    background: linear-gradient(180deg, rgba(126,184,48,0) 0%, rgba(126,184,48,0.55) 45%, #7db830 100%);
  }
</style>
</head>
<body>
  <main class="flyer">
    <div class="hero-photo" role="img" aria-label="Aerial view of an apartment courtyard with artificial turf dog run, paver patios, lounge seating and planted beds"></div>

    <svg class="wave" viewBox="0 0 758 981" aria-hidden="true">
      <path d="M0,512 C70,478 160,468 230,488 L250,496 C300,438 380,380 480,370 C590,360 690,410 758,486 L758,981 L0,981 Z" fill="var(--ink)"/>
      <path d="M0,512 C70,478 160,468 230,488 L250,496 C300,438 380,380 480,370 C590,360 690,410 758,486" fill="none" stroke="var(--lime)" stroke-width="4"/>
    </svg>

    <div class="logo">
      <span class="logo-name">Verdant Grade</span>
      <span class="logo-tagline">LANDSCAPE AND IRRIGATION</span>
    </div>

    <div class="project-photo project-photo--roadside"><span role="img" aria-label="Roadside rock bed planting beside a sports field fence"></span></div>
    <div class="project-photo project-photo--clubhouse"><span role="img" aria-label="Clubhouse entrance with flowering shrubs and fresh lawn"></span></div>
    <div class="project-photo project-photo--station"><span role="img" aria-label="Fuel station frontage with river rock and ornamental grasses"></span></div>

    <p class="markets">
      COMMERCIAL<span class="dot">•</span>GOVERNMENT<span class="dot">•</span>RESIDENTIAL<br>
      MUNICIPALITY<span class="dot">•</span>SPORTS FIELDS
    </p>

    <h2 class="section-title section-title--about">ABOUT US</h2>
    <p class="about-text">
      Our businesses are dedicated to completing their project on time, running efficiently, and we do excellent work. Our average commercial landscape installation size is <strong>$215,000</strong> with our largest completed in 2020 being <strong>$1,375,590</strong>.&nbsp; We have backgrounds in commercial design and installation and help our customers with Value Engineering Strategies. Since incorporated in 2005, <strong>we have an average employment retention length of 8 years.</strong>
    </p>

    <h2 class="section-title section-title--services">OUR SERVICES</h2>

    <div class="service service--turf">
      <svg viewBox="0 0 36 36" fill="none" stroke="var(--lime)" stroke-width="1.6" aria-hidden="true">
        <circle cx="9" cy="25" r="6"/><circle cx="9" cy="25" r="2.5"/>
        <circle cx="17" cy="14" r="6"/><circle cx="17" cy="14" r="2.5"/>
        <path d="M15 25 H33 V31 H9"/><path d="M23 14 H33 V20"/>
      </svg>
      TURF MANAGEMENT
    </div>
    <div class="service service--hardscape">
      <svg viewBox="0 0 36 36" fill="none" stroke="var(--lime)" stroke-width="1.6" aria-hidden="true">
        <rect x="4" y="4" width="28" height="28" rx="2"/>
        <path d="M4 14 L14 10 L20 16 L32 12"/><path d="M14 10 V4"/><path d="M20 16 L16 26 L4 24"/>
        <path d="M16 26 L24 32"/><path d="M20 16 L32 22"/>
      </svg>
      HARDSCAPING
    </div>
    <div class="service service--irrigation">
      <svg viewBox="0 0 36 36" fill="none" stroke="var(--lime)" stroke-width="1.6" aria-hidden="true">
        <path d="M18 14 V30"/><rect x="14" y="10" width="8" height="5"/>
        <path d="M14 12 L6 6"/><path d="M22 12 L30 6"/><path d="M18 10 V3"/>
        <path d="M3 31 H33"/><path d="M6 31 L8 25 M10 31 L10 26 M26 31 L27 25 M30 31 L29 26"/>
      </svg>
      IRRIGATION
    </div>
    <div class="service service--landscape">
      <svg viewBox="0 0 36 36" fill="none" stroke="var(--lime)" stroke-width="1.6" aria-hidden="true">
        <path d="M12 18 L18 12 L24 18 V24 H12 Z"/>
        <ellipse cx="6" cy="12" rx="3" ry="6"/><path d="M6 18 V24"/>
        <ellipse cx="30" cy="12" rx="3" ry="6"/><path d="M30 18 V24"/>
        <path d="M3 24 H33"/><path d="M18 24 L18 34 M14 24 L8 34 M22 24 L28 34"/>
      </svg>
      LANDSCAPING
    </div>

    <svg class="safety-badge" viewBox="0 0 132 115" aria-label="EMR safety rating .72">
      <path d="M66 2 L110 14 V60 C110 82 90 100 66 112 C42 100 22 82 22 60 V14 Z" fill="var(--lime)"/>
      <path d="M66 9 L103 19 V58 C103 76 87 91 66 102 C45 91 29 76 29 58 V19 Z" fill="none" stroke="var(--ink)" stroke-width="2"/>
      <text x="66" y="58" text-anchor="middle" font-family="Ubuntu, sans-serif" font-weight="700" font-size="40" fill="var(--ink)">.72</text>
      <path d="M4 78 L16 70 L66 66 L116 70 L128 78 L118 82 L124 90 L66 86 L8 90 L14 82 Z" fill="var(--lime)" stroke="var(--ink)" stroke-width="1.5"/>
      <text x="66" y="82" text-anchor="middle" font-family="Ubuntu, sans-serif" font-weight="700" font-size="11" fill="var(--ink)">EMR SAFETY RATING</text>
    </svg>

    <div class="call-bar">
      <strong>CALL :</strong>&nbsp;Oakridge Office&nbsp;<strong>1-555-201-4187,</strong>&nbsp;&nbsp;Millbrook Office&nbsp;<strong>1-555-318-7702</strong>
    </div>

    <div class="contact-line">
      <span class="contact-item">
        <svg viewBox="0 0 14 14" fill="none" stroke="var(--lime)" stroke-width="1.4" aria-hidden="true"><path d="M7 13 C3 8 2 6.5 2 5 A5 5 0 0 1 12 5 C12 6.5 11 8 7 13 Z"/><circle cx="7" cy="5" r="1.8"/></svg>
        PO Box 400120 Oakridge, KS 66000
      </span>
      <span class="contact-item">
        <svg viewBox="0 0 14 14" fill="none" stroke="var(--lime)" stroke-width="1.2" aria-hidden="true"><circle cx="7" cy="7" r="6"/><ellipse cx="7" cy="7" rx="2.6" ry="6"/><path d="M1 7 H13 M2 4 H12 M2 10 H12"/></svg>
        verdantgradeinc.com
      </span>
      <span class="contact-item">
        <svg viewBox="0 0 14 14" fill="none" stroke="var(--lime)" stroke-width="1.3" aria-hidden="true"><circle cx="7" cy="7" r="6"/><circle cx="7" cy="7" r="2.2"/><path d="M9.2 5 V8 C9.2 9.4 11 9.4 11 8"/></svg>
        office@verdantgradeinc.com
      </span>
    </div>

    <div class="grass-strip" role="img" aria-label="Band of green grass blades along the bottom edge"></div>
  </main>
</body>
</html>
```